Redesign one screen in a mobile app

I have an app called Toasts and Tallies (available on iOS and Android). This app allows wedding guests to bet on things that happen during a wedding they are attending (think: will the groom cry when the bride walks down the aisle...). The event is set up by someone called the "event leader", typically this is the bride or the groom.

Once event details, bets, and $ values of the bets are entered, the event leader publishes the event and gets to the event detail homescreen, where they can manage their event. The three main things they can do are:

1.) Share the event with other guests to join in the betting.
2.) Edit the event -- add, change, or delete bets.
3.) Add a co-organizer. If you are the bride or the groom, you want someone else managing the event on your wedding day.

I'd like to redesign this page, make it simpler, and *focus attention on sharing the event.* The biggest goal of this page is getting event leaders to share the event. We want them to invite as many wedding guests as possible.

To that end, I would like to also introducing "sharing tiers" to entice more sharing and I'd like this to be something event leaders can easily see once they hit the event homescreen. Tiers are as follows:
Share with 1 guest, unlock co-organizer feature.
Share with 5 guests, unlock physical placard with custom QR code.
Share with 10 guests, we split our proceeds with the bride and groom.
Share with 20 guests, you are entered into $250 monthly raffle.

Some additional requests:
+ Please do not use current fonts. We want new fonts that are cleaner.
+ Share options should stay the same (copy, share, QR code)
+ Need to keep "help" question mark on page as well.
+ Maintain colors generally. Red button color must be kept as is because it's used throughout app. Slight variations to other colors OK.
+ Navigation at bottom must remain.
+ Feel free to add moving elements as well, like gifs.
+ Final design delivered in Figma.
Updates

Submissions need to be app designs. Not webpages.

The current actions shown on the page need to remain - share event, edit event, add a Co-Organizer. But the goal of the design is to make the page simpler, not more complicated.

Sharing tiers can be a separate screen, linked from the event home screen. This information does not need to live on the same page!

Target Market(s)

25-40 year olds

Industry/Entity Type

Mobile Apps - Betting

Font styles to use
Sans Serif
Other font styles liked:
• I like poppins, but open to other options.

Requirements
Must have
• Fun design that focuses on sharing an event. Design delievered in Figma.

```html
<!DOCTYPE html>
<html lang="en">
<head>
<meta charset="utf-8">
<title>Toasts and Tallies – Event Home</title>
<link rel="stylesheet" href="https://fonts.googleapis.com/css2?family=Poppins:wght@400;500;600&display=swap">
<style>
:root{
  --brand-red:#e05a4f;
  --brand-red-soft:#e8766b;
  --header-red:#e0655a;
  --page-bg:#fbe3e0;
  --screen-bg:#f5f5f5;
  --card:#ffffff;
  --ink:#4a4a4a;
  --ink-soft:#8a8a8a;
  --ink-faint:#b3b3b3;
  --line:#e6e6e6;
  --chip:#efefef;
  --panel-pink:#fdeceb;
}
*{box-sizing:border-box;margin:0;padding:0}
html,body{width:1200px;height:2455px;overflow:hidden}
body{background:var(--page-bg);font-family:'Poppins',sans-serif;color:var(--ink);position:relative}
.abs{position:absolute}
.screen{position:absolute;left:360px;top:190px;width:558px;height:2090px;background:var(--screen-bg);overflow:hidden;border-radius:40px 40px 0 0}
.header{position:absolute;left:0;top:0;width:558px;height:150px;background:linear-gradient(120deg,#e9786d 0%,var(--header-red) 45%,#df5d52 100%)}
.round-btn{position:absolute;width:42px;height:42px;border-radius:50%;background:#fff;display:flex;align-items:center;justify-content:center;box-shadow:0 2px 6px rgba(0,0,0,.12)}
.body{position:absolute;left:0;top:138px;width:558px;height:1952px;background:var(--screen-bg);border-radius:12px 12px 0 0}
.section-title{position:absolute;left:33px;font-size:25px;font-weight:500;color:#505050;line-height:1}
.card{position:absolute;left:35px;width:488px;background:var(--card);border-radius:6px;box-shadow:0 1px 4px rgba(0,0,0,.05)}
.event-photo{position:absolute;left:22px;top:15px;width:146px;height:145px;border-radius:6px;background:linear-gradient(180deg,#b9a9a2 0%,#7f7a76 55%,#5e5b59 100%)}
.event-name{position:absolute;left:200px;top:38px;font-size:19px;font-weight:500;color:#4a4a4a}
.meta{position:absolute;font-size:13px;color:var(--ink-faint);display:flex;align-items:center;gap:6px;line-height:1}
.divider{position:absolute;left:22px;right:20px;top:184px;height:1px;background:var(--line)}
.chip{position:absolute;left:22px;top:203px;width:88px;height:39px;border-radius:5px;background:var(--chip);font-size:11px;color:var(--ink-soft);display:flex;align-items:center;justify-content:center;gap:6px}
.share-copy{position:absolute;left:0;width:488px;text-align:center;line-height:1}
.url-box{position:absolute;left:22px;top:153px;width:445px;height:40px;border-radius:5px;background:var(--chip);font-size:12px;color:var(--ink-soft);display:flex;align-items:center;gap:6px;padding-left:12px;white-space:nowrap}
.btn{position:absolute;height:39px;border-radius:5px;background:var(--brand-red);color:#fff;font-size:13px;font-weight:500;display:flex;align-items:center;justify-content:center;box-shadow:0 2px 4px rgba(224,90,79,.25)}
.tier{position:absolute;background:#fff;border-radius:3px;overflow:hidden;text-align:center}
.tier-title{font-size:17px;font-weight:500;line-height:1}
.tier-text{font-size:14px;line-height:22px;color:#666}
.tier-foot{position:absolute;left:0;right:0;bottom:0;height:37px;background:var(--brand-red);color:#fff;font-size:16px;display:flex;align-items:center;justify-content:space-between;padding:0 24px}
.tier.active{background:var(--brand-red);color:#fff;box-shadow:0 6px 14px rgba(0,0,0,.18)}
.tier.active .tier-text{color:#fff}
.tier.active .tier-foot{background:var(--brand-red-soft);border-top:1px solid rgba(255,255,255,.3)}
.steps{position:absolute;list-style:none}
.step{position:absolute;display:flex;gap:16px;font-size:15.5px;line-height:26px;color:#555}
.num{flex:none;width:24px;height:24px;border-radius:50%;background:var(--brand-red);color:#fff;font-size:11px;font-weight:600;display:flex;align-items:center;justify-content:center;margin-top:1px}
.illustration{position:absolute;border-radius:8px}
.organizers{position:absolute;left:0;top:243px;width:486px;height:149px;background:var(--panel-pink)}
.nav{position:absolute;left:0;top:2015px;width:558px;height:75px;background:#fff;border-radius:18px 18px 0 0;box-shadow:0 -2px 8px rgba(0,0,0,.05)}
.nav-item{position:absolute;top:14px;width:100px;margin-left:-50px;display:flex;flex-direction:column;align-items:center;gap:4px;font-size:13px;color:#777}
.nav-item.current{color:var(--brand-red)}
</style>
</head>
<body>
<main class="screen">
  <header class="header">
    <div class="round-btn" style="left:34px;top:63px" aria-label="Back">
      <svg width="18" height="18" viewBox="0 0 18 18" fill="none" stroke="#555" stroke-width="1.8" stroke-linecap="round" stroke-linejoin="round"><path d="M15 9H3M8 4L3 9l5 5"/></svg>
    </div>
    <div class="round-btn" style="left:483px;top:63px" aria-label="Help">
      <svg width="20" height="20" viewBox="0 0 20 20" fill="none" stroke="#555" stroke-width="1.5" stroke-linecap="round"><circle cx="10" cy="10" r="8.5"/><path d="M7.8 7.6a2.3 2.3 0 1 1 3.2 2.1c-.7.3-1 .8-1 1.5v.6"/><circle cx="10" cy="14.4" r=".5" fill="#555"/></svg>
    </div>
  </header>

  <section class="body"></section>

  <!-- Event details -->
  <h2 class="section-title" style="top:178px">Event Details</h2>
  <article class="card" style="top:224px;height:260px">
    <div class="event-photo" role="img" aria-label="Photo of a tree-lined street in winter with a car driving"></div>
    <h3 class="event-name">Oak Drive</h3>
    <div class="meta" style="left:200px;top:85px">
      <svg width="13" height="13" viewBox="0 0 13 13" fill="none" stroke="#bbb" stroke-width="1.2"><rect x="1" y="2" width="11" height="10" rx="1.5"/><path d="M1 5h11M4 .5v3M9 .5v3"/></svg>Feb 08
    </div>
    <div class="meta" style="right:25px;top:85px">
      <svg width="13" height="13" viewBox="0 0 13 13" fill="none" stroke="#bbb" stroke-width="1.2"><circle cx="6.5" cy="6.5" r="5.5"/><path d="M6.5 3.5v3h2.5"/></svg>05:00 PM
    </div>
    <div class="meta" style="left:200px;top:121px">
      <svg width="12" height="13" viewBox="0 0 12 13" fill="none" stroke="#bbb" stroke-width="1.2"><path d="M6 12s4-4 4-7a4 4 0 0 0-8 0c0 3 4 7 4 7z"/><circle cx="6" cy="5" r="1.4"/></svg>&nbsp;Missouri
    </div>
    <div class="divider"></div>
    <div class="chip">
      <svg width="15" height="15" viewBox="0 0 15 15" fill="none" stroke="#aaa" stroke-width="1.2" stroke-linejoin="round"><path d="M7.5 1l5 5-5 8-5-8z"/><path d="M2.5 6l5 3 5-3"/></svg>3 Bets
    </div>
  </article>

  <!-- Share -->
  <h2 class="section-title" style="top:525px">Share Your Events</h2>
  <div class="illustration" style="left:497px;top:540px;width:42px;height:62px;background:linear-gradient(180deg,#e8554a 0%,#f2c9a8 40%,#f1d2b6 100%);border-radius:18px" role="img" aria-label="Small hand making a finger-heart gesture"></div>
  <article class="card" style="top:578px;height:268px">
    <p class="share-copy" style="top:26px;font-size:14.5px;color:#555">Invite guests to join the event by sharing the link below.</p>
    <p class="share-copy" style="top:55px;font-size:17.5px;font-weight:600;color:var(--brand-red)">Each guest pays $2.99 to join.</p>
    <p class="share-copy" style="top:88px;font-size:14.5px;line-height:26px;color:#999">If 10 or more guests participate, proceeds will be shared<br>with the bride and groom!</p>
    <div class="url-box">
      <svg width="14" height="14" viewBox="0 0 14 14" fill="none" stroke="#999" stroke-width="1.2" stroke-linecap="round"><path d="M6 8a3 3 0 0 0 4 0l2-2a3 3 0 0 0-4-4l-1 1"/><path d="M8 6a3 3 0 0 0-4 0L2 8a3 3 0 0 0 4 4l1-1"/></svg>
      https://links.toastsandtallies.com/7qTbWd42KpR9nmLYE
    </div>
    <div class="btn" style="left:22px;top:208px;width:143px">Copy</div>
    <div class="btn" style="left:174px;top:208px;width:142px">Share</div>
    <div class="btn" style="left:325px;top:208px;width:142px">QR Code</div>
  </article>

  <!-- Sharing tiers -->
  <h2 class="section-title" style="top:899px">Sharing Tiers</h2>
  <svg class="abs" style="left:460px;top:902px" width="70" height="22" viewBox="0 0 70 22" fill="none" stroke-width="2" stroke-linecap="round" stroke-linejoin="round">
    <path d="M27 11H3M10 4l-7 7 7 7" stroke="#bbb"/>
    <path d="M39 11h24M56 4l7 7-7 7" stroke="#444"/>
  </svg>

  <div class="tier" style="left:-115px;top:968px;width:257px;height:155px">
    <p class="tier-title" style="margin-top:27px">Share with 1 guest</p>
    <p class="tier-text" style="margin-top:8px">Unlock co-organizer<br>feature</p>
    <div class="tier-foot"><span>Share</span>
      <svg width="20" height="20" viewBox="0 0 20 20" fill="#fff"><circle cx="15" cy="4" r="3"/><circle cx="5" cy="10" r="3"/><circle cx="15" cy="16" r="3"/><path d="M5 10l10-6M5 10l10 6" stroke="#fff" stroke-width="2"/></svg>
    </div>
  </div>

  <div class="tier active" style="left:151px;top:960px;width:258px;height:170px">
    <p class="tier-title" style="margin-top:30px;font-size:19px">Share with 5 guest</p>
    <p class="tier-text" style="margin-top:8px;font-size:15px">Unlock physical placard<br>with custom QR code</p>
    <div class="tier-foot" style="height:42px;font-size:17px"><span>Share</span>
      <svg width="20" height="20" viewBox="0 0 20 20" fill="#fff"><circle cx="15" cy="4" r="3"/><circle cx="5" cy="10" r="3"/><circle cx="15" cy="16" r="3"/><path d="M5 10l10-6M5 10l10 6" stroke="#fff" stroke-width="2"/></svg>
    </div>
  </div>

  <div class="tier" style="left:417px;top:968px;width:257px;height:155px">
    <p class="tier-title" style="margin-top:27px">Share with 10 guests</p>
    <p class="tier-text" style="margin-top:8px">We split our proceeds with<br>the bride and groom</p>
    <div class="tier-foot"><span>Share</span>
      <svg width="20" height="20" viewBox="0 0 20 20" fill="#fff"><circle cx="15" cy="4" r="3"/><circle cx="5" cy="10" r="3"/><circle cx="15" cy="16" r="3"/><path d="M5 10l10-6M5 10l10 6" stroke="#fff" stroke-width="2"/></svg>
    </div>
  </div>

  <!-- Edit -->
  <h2 class="section-title" style="top:1201px;left:34px">Edit Your Event</h2>
  <article class="card" style="top:1252px;height:234px;width:486px">
    <div class="step" style="left:22px;top:21px"><span class="num">1</span>Change event details</div>
    <div class="step" style="left:22px;top:60px"><span class="num">2</span>Add or delete bets</div>
    <div class="step" style="left:22px;top:98px"><span class="num">3</span>Change answer choices</div>
    <div class="btn" style="left:23px;top:163px;width:141px;font-size:12.5px">Edit Your Event</div>
    <div class="illustration" style="left:262px;top:38px;width:205px;height:196px;background:linear-gradient(180deg,#f4b7ae 0%,#fbe6e3 60%,#fff 100%)" role="img" aria-label="Line illustration of a cheering woman raising both fists"></div>
  </article>

  <!-- Co-organizer -->
  <h2 class="section-title" style="top:1519px;left:34px">Assign a Co-Organizer</h2>
  <article class="card" style="top:1570px;height:392px;width:486px;overflow:hidden">
    <div class="illustration" style="left:0;top:30px;width:195px;height:210px;background:linear-gradient(180deg,#f4b2a8 0%,#fbe4e1 55%,#fff 100%)" role="img" aria-label="Line illustration of a smiling man pointing to the right"></div>
    <div class="step" style="left:199px;top:37px;width:270px"><span class="num">1</span>Bride/Groom-created event? Assign a co-organizer.</div>
    <div class="step" style="left:199px;top:105px;width:270px"><span class="num">2</span>Co-organizer manages bets during wedding weekend.</div>
    <div class="step" style="left:199px;top:171px;width:270px"><span class="num">3</span>Co-organizer notified to take over.</div>
    <div class="organizers">
      <h3 class="abs" style="left:21px;top:24px;font-size:18px;font-weight:500;color:#555">Event Organizers</h3>
      <div class="round-btn" style="left:422px;top:17px;width:42px;height:42px" aria-label="Add organizer">
        <svg width="14" height="14" viewBox="0 0 14 14" stroke="#444" stroke-width="2" stroke-linecap="round"><path d="M7 2v10M2 7h10"/></svg>
      </div>
      <div class="abs" style="left:22px;top:70px;width:54px;height:54px;border-radius:50%;background:linear-gradient(160deg,#c9b8a8,#6d5a4c)" role="img" aria-label="Profile photo of the organizer"></div>
      <p class="abs" style="left:93px;top:85px;font-size:17px;font-weight:500;color:#555">Marco Lindqvist</p>
    </div>
  </article>

  <!-- Bottom navigation -->
  <nav class="nav">
    <div class="nav-item current" style="left:74px">
      <svg width="28" height="26" viewBox="0 0 28 26" fill="none" stroke="currentColor" stroke-width="1.8" stroke-linejoin="round"><path d="M3 12L14 3l11 9M6 10v13h16V10"/><path d="M11 23v-7h6v7"/></svg>Home
    </div>
    <div class="nav-item" style="left:278px">
      <svg width="26" height="28" viewBox="0 0 26 28" fill="none" stroke="#666" stroke-width="1.8" stroke-linejoin="round"><path d="M13 2l9 9-9 15-9-15z"/><path d="M4 11l9 6 9-6"/></svg>My Bets
    </div>
    <div class="nav-item" style="left:482px">
      <svg width="44" height="28" viewBox="0 0 44 28" fill="none" stroke="#666" stroke-width="1.6"><circle cx="22" cy="8" r="5"/><path d="M13 26c0-6 4-9 9-9s9 3 9 9"/><circle cx="9" cy="11" r="4"/><path d="M2 25c0-4 3-7 7-7"/><circle cx="35" cy="11" r="4"/><path d="M42 25c0-4-3-7-7-7"/></svg>Leaders
    </div>
  </nav>
</main>
</body>
</html>
```